Young, dynamic furniture company needs a new business card design

We require a new business card design for our modern furniture company which supplies furniture and appliances to the property and development market.
Quillmere Furnishing has become one of the leading furniture & appliance suppliers to the property market withing London. With over 10 years experience, we have increased our business to supply not only private landlords and managing agents, but also property developers, housing associations and local councils.
We offer not only a complete range of furniture which includes beds, wardrobes, dining sets and sofas, but also a high quality, full delivery and assembly service to help you with all our furnishing needs.

Target Market(s)

Private landlords, estate agents, letting agents, property management companies

Industry/Entity Type

Business

Contact Information for Business Card

Name,
Title,
Address,
Mobile,
Telephone,
Fax, Website, email address

Font styles to use
Sans Serif

Colors
3176b5
0555a3
85abd2
cfdeed

Requirements
Must have
• All the above information for each of our staff, along with our logo

```html
<!DOCTYPE html>
<html lang="en">
<head>
<meta charset="utf-8">
<title>Quillmere Furnishing – Business Card</title>
<link href="https://fonts.googleapis.com/css2?family=Open+Sans:wght@400;600&display=swap" rel="stylesheet">
<style>
  :root {
    --page-bg: #e4e6ea;
    --card-edge: #2b2c2f;
    --brand-blue: #0555a3;
    --panel-blue: #3176b5;
    --line-blue: #85abd2;
    --logo-tile: #cfdeed;
    --ink-dark: #262a38;
    --white: #ffffff;
  }
  * { box-sizing: border-box; margin: 0; padding: 0; }
  html, body { width: 1200px; height: 1000px; overflow: hidden; }
  body {
    background: var(--page-bg);
    font-family: "Open Sans", Arial, sans-serif;
    position: relative;
  }
  .card {
    position: absolute;
    left: 270px;
    width: 660px;
    height: 380px;
    background: var(--card-edge);
    border-radius: 4px;
    padding: 14px;
  }
  .card--front { top: 80px; }
  .card--back { top: 530px; }
  .card__face {
    position: relative;
    width: 100%;
    height: 100%;
    background: var(--brand-blue);
    border-radius: 24px;
    overflow: hidden;
  }
  .holder { position: absolute; left: 72px; top: 36px; color: var(--white); }
  .holder__name { font-size: 24px; font-weight: 400; letter-spacing: 0.5px; line-height: 1.1; }
  .holder__title { font-size: 13px; opacity: 0.9; }
  .brand-tile {
    position: absolute;
    background: var(--logo-tile);
    display: flex;
    align-items: center;
    justify-content: center;
    flex-direction: column;
    gap: 10px;
    color: var(--ink-dark);
    text-align: center;
  }
  .brand-tile__mark { width: 26px; height: 26px; background: var(--ink-dark); }
  .brand-tile__name { font-size: 14px; font-weight: 600; letter-spacing: 0.3px; }
  .card--front .brand-tile { left: 54px; top: 92px; width: 200px; height: 150px; }
  .card--back .brand-tile { left: 50%; top: 50%; width: 226px; height: 176px; transform: translate(-50%, -50%); }
  .card--back .brand-tile__name { font-size: 16px; }
  .contact-panel {
    position: absolute;
    right: 0;
    top: 66px;
    width: 292px;
    height: 222px;
    background: var(--panel-blue);
    border-bottom: 18px solid var(--brand-blue);
    color: var(--white);
    padding: 20px 0 0 22px;
    font-size: 13px;
    line-height: 1.25;
  }
  .contact-row { display: flex; align-items: flex-start; gap: 14px; position: relative; }
  .contact-row + .contact-row { margin-top: 10px; }
  .contact-row__icon { width: 24px; height: 24px; flex: none; }
  .contact-row__text { padding-bottom: 10px; border-bottom: 1px solid var(--line-blue); width: 190px; }
  .contact-row--address .contact-row__text { padding-top: 5px; padding-bottom: 22px; }
</style>
</head>
<body>
  <section class="card card--front">
    <div class="card__face">
      <div class="holder">
        <div class="holder__name">NAME</div>
        <div class="holder__title">Title</div>
      </div>
      <div class="brand-tile">
        <span class="brand-tile__mark"></span>
        <span class="brand-tile__name">QUILLMERE FURNISHING</span>
      </div>
      <div class="contact-panel">
        <div class="contact-row">
          <svg class="contact-row__icon" viewBox="0 0 24 24" fill="none" stroke="#fff" stroke-width="1.6">
            <rect x="1" y="1" width="22" height="22" rx="5"/>
            <path d="M8 6.5c-1 .6-1.5 1.6-1 3 1 2.6 3 4.8 5.6 6 1.3.5 2.4 0 3-1l-2-2-1.4.8c-1.2-.6-2.1-1.5-2.7-2.7l.8-1.4z" fill="#fff" stroke="none"/>
          </svg>
          <div class="contact-row__text">T: 00 142 468 568<br>M: 00 452 568 862<br>F: 00 555 555 555</div>
        </div>
        <div class="contact-row">
          <svg class="contact-row__icon" viewBox="0 0 24 24" fill="none" stroke="#fff" stroke-width="1.6">
            <rect x="1" y="1" width="22" height="22" rx="5"/>
            <circle cx="12" cy="12" r="5.5" fill="#fff" stroke="none"/>
            <path d="M9 10.5c1 .2 1.5 1 2.5.7M13 14.5c.8-.6 1.6-.2 2-1" stroke="#3176b5" stroke-width="1.2"/>
          </svg>
          <div class="contact-row__text">WWW.WEBSITE.COM<br>INFO@EMAIL.COM</div>
        </div>
        <div class="contact-row contact-row--address">
          <svg class="contact-row__icon" viewBox="0 0 24 24" fill="none" stroke="#fff" stroke-width="1.6">
            <rect x="1" y="1" width="22" height="22" rx="5"/>
            <path d="M5.5 12 12 6.5 18.5 12v6h-13z" fill="#fff" stroke="none"/>
            <rect x="10.5" y="14" width="3" height="4" fill="#3176b5" stroke="none"/>
          </svg>
          <div class="contact-row__text">ADDRESS</div>
        </div>
      </div>
    </div>
  </section>

  <section class="card card--back">
    <div class="card__face">
      <div class="brand-tile">
        <span class="brand-tile__mark"></span>
        <span class="brand-tile__name">QUILLMERE FURNISHING</span>
      </div>
    </div>
  </section>
</body>
</html>
```